Heron Dusk business card design

I make handmade colourful women's beaded jewellery (necklaces and earnings).
I require a business card to be designed to truly reflect my jewellery, that is, it is different and stands out.
I would like the business card to look creative, arty, gentle and feminine and fit in with the look of my website and logo (already developed).
I would like the business card to have strong use of the water reeds that are flowing in the wind (please see the banner image on my website www.herondusk-example.com and attached files).

Target Market(s)

Women who are fashion conscious, hip and funky. My audience like things that are a little different and stand out in a crowd.These women are aged in their 20's-40's.

Industry/Entity Type

Jewelry

Contact Information for Business Card

Please include the following items:
1) my logo: Heron Dusk
2) my name, address and phone number: Marla Dorsten, Sydney, Australia, 0400 000 000
3) my web details: www.herondusk-example.com, info@herondusk-example.com, www.facebook.com/herondusk

Font styles to use
Other font styles liked:
• Remachine Script

Requirements
Must have
• My business card must have the following:
• 1) my personal details including all my website contacts (see above).
• 2) Heron Dusk logo
• 3) Reeds flowing in the wind (see my banner image on my website www.herondusk-example.com or see attached files).
Nice to have
• A sunrise in the background (rising over water)
• I would prefer that the colour scheme to fit with the Heron Dusk logo, that is the colours of an early morning sunrise i.e yellows, oranges. The use of black and white is fine.
Should not have
• I do not like a commercial manufactured look with hard edges. I would like a look that is soft and reflects an artistic, creative and independent business.

```html
<!DOCTYPE html>
<html lang="en">
<head>
<meta charset="utf-8">
<title>Heron Dusk – Business Card</title>
<link href="https://fonts.googleapis.com/css2?family=Arimo:wght@400;700&display=swap" rel="stylesheet">
<style>
  :root{
    --backdrop:#2b2b2b;
    --paper:#ffffff;
    --ink:#1e1e1e;
    --ink-soft:#6b6b6b;
    --accent:#f5a300;
    --sun-light:#ffe14a;
    --sun-mid:#ffc31a;
    --sun-deep:#f28c00;
    --water:#f7a21c;
    --rule:#bdbdbd;
    --dot:#9a9a9a;
  }
  *{box-sizing:border-box;margin:0;padding:0}
  html,body{width:1200px;height:950px;overflow:hidden}
  body{
    background:var(--backdrop);
    font-family:"Arimo",Arial,sans-serif;
    display:flex;flex-direction:column;align-items:center;justify-content:center;gap:30px;
  }
  .card{
    position:relative;width:760px;height:434px;background:var(--paper);
    overflow:hidden;box-shadow:0 10px 30px rgba(0,0,0,.45);
  }
  .brand-name{font-weight:400;color:var(--ink);line-height:1.1;white-space:nowrap}

  /* front */
  .front .brand{
    position:absolute;left:0;right:0;top:58px;
    display:flex;flex-direction:column;align-items:center;gap:12px;
  }
  .front .brand-name{font-size:30px}
  .front .brand-disc{
    width:150px;height:150px;border-radius:50%;
    background:var(--sun-mid);
  }
  .front .social-row{
    position:absolute;left:90px;right:90px;top:330px;
    display:flex;align-items:center;gap:10px;
  }
  .front .social-row .rule{flex:1;height:1px;background:var(--rule)}
  .front .social-dot{width:20px;height:20px;border-radius:50%;background:var(--dot)}

  /* back */
  .back .sun-scene{
    position:absolute;left:392px;top:-62px;width:456px;height:456px;border-radius:50%;
    background:
      linear-gradient(180deg,
        var(--sun-light) 0%,
        var(--sun-mid) 48%,
        var(--sun-deep) 62%,
        var(--water) 70%,
        var(--sun-deep) 82%,
        var(--water) 100%);
  }
  .back .brand-name{position:absolute;left:52px;top:72px;font-size:38px}
  .back .person{position:absolute;left:52px;top:186px}
  .person-name{font-size:22px;color:var(--ink);line-height:1.2}
  .person-role{font-size:16px;color:var(--accent);margin-top:3px}
  .address{margin-top:14px;font-size:15px;color:var(--ink-soft);line-height:1.35}
  .contact-list{list-style:none;margin-top:8px}
  .contact-list li{display:flex;align-items:center;gap:10px;font-size:15px;color:var(--ink-soft);line-height:1.75;white-space:nowrap}
  .contact-list svg{width:15px;height:15px;flex:none}
</style>
</head>
<body>

<section class="card front" aria-label="Card front">
  <div class="brand">
    <div class="brand-name">Heron Dusk</div>
    <div class="brand-disc"></div>
  </div>
  <div class="social-row">
    <span class="rule"></span>
    <span class="social-dot"></span>
    <span class="social-dot"></span>
    <span class="social-dot"></span>
    <span class="social-dot"></span>
    <span class="rule"></span>
  </div>
</section>

<section class="card back" aria-label="Card back">
  <div class="sun-scene" role="img" aria-label="Early morning sunrise over water, with water reeds flowing in the wind and a heron silhouette perched on a post"></div>

  <div class="brand-name">Heron Dusk</div>

  <div class="person">
    <div class="person-name">Lena Harrow</div>
    <div class="person-role">President</div>
    <div class="address">Marla Dorsten<br>Sydney, Australia</div>
    <ul class="contact-list">
      <li>
        <svg viewBox="0 0 16 16"><path d="M3 1h3l1 4-2 1c1 2 3 4 5 5l1-2 4 1v3c0 1-1 2-2 2C7 15 1 9 1 3c0-1 1-2 2-2z" fill="#1e1e1e"/></svg>
        0400 000 000
      </li>
      <li>
        <svg viewBox="0 0 16 16"><rect x="1" y="3" width="14" height="10" fill="#1e1e1e"/><path d="M1 3l7 6 7-6" stroke="#fff" stroke-width="1.3" fill="none"/></svg>
        info@herondusk-example.com
      </li>
      <li>
        <svg viewBox="0 0 16 16"><circle cx="8" cy="8" r="7" fill="#1e1e1e"/><path d="M1 8h14M8 1c-3 3-3 11 0 14M8 1c3 3 3 11 0 14" stroke="#fff" stroke-width="1" fill="none"/></svg>
        www.herondusk-example.com
      </li>
      <li>
        <svg viewBox="0 0 16 16"><rect x="1" y="1" width="14" height="14" fill="#1e1e1e"/></svg>
        herondusk
      </li>
    </ul>
  </div>
</section>

</body>
</html>
```